Flyer-Design für Kaffeehaus
Zielgruppe
Wir sind ein Kaffeehaus und suchen ein super Design als Hintergrund für einen Jazz Brunch.
Zielgruppe Jung bis alt.
Aufgabenstellung
Schlicht, einfach, aber doch ausgefallen und modern.
Das Thema Jazz muss zwingend darin wiederSpiegeln und eventuell auch einen Hauch von Frühstück.
Jazz Bruch, live Jazz Musik mit Frühstück von 10-13 Uhr.
Ausgefallene aber leicht leserliche Schrift.
Benötigte Formate sind A6 A4 A3 und Titelbild und Profilbild Format für Facebook.

```html
<!DOCTYPE html>
<html lang="de">
<head>
<meta charset="utf-8">
<title>Jazz Brunch – Flyer</title>
<link href="https://fonts.googleapis.com/css2?family=Bitter:wght@700;800&family=Cabin:wght@500;600&display=swap" rel="stylesheet">
<style>
  :root {
    --page: #ffffff;
    --paper: #e4e0dc;
    --orange: #e86f47;
    --brown: #6a3f1a;
    --ink: #5a3312;
    --light: #ebe6e1;
    --sketch: #8a5a33;
    --sketch-soft: #cdb8a4;
  }
  * { margin: 0; padding: 0; box-sizing: border-box; }
  html, body { width: 1200px; height: 848px; overflow: hidden; background: var(--page); }
  .canvas { position: relative; width: 1200px; height: 848px; }

  .flyer {
    position: absolute; top: 138px; width: 404px; height: 571px;
    background: var(--paper); overflow: hidden;
    box-shadow: 0 4px 18px rgba(0,0,0,0.12);
  }
  .flyer--a { left: 138px; }
  .flyer--b { left: 658px; }

  .art { position: absolute; border-radius: 10px; opacity: 0.9; }
  .art--sax { left: 0; top: 0; width: 102px; height: 183px;
    background: linear-gradient(160deg, var(--sketch-soft), var(--sketch)); border-radius: 0 0 30px 0; }
  .art--reed { left: 123px; top: 0; width: 52px; height: 23px;
    background: linear-gradient(90deg, var(--sketch-soft), var(--sketch)); border-radius: 0 0 12px 12px; }
  .art--tuba { right: 0; top: 39px; width: 128px; height: 107px;
    background: linear-gradient(200deg, var(--sketch), var(--sketch-soft)); border-radius: 50px 0 0 50px; }
  .art--cup { right: 0; top: 284px; width: 70px; height: 63px;
    background: linear-gradient(160deg, var(--sketch-soft), var(--sketch)); border-radius: 12px 12px 24px 24px; }
  .flyer--b .art--tuba { top: 58px; }
  .flyer--b .art--cup { top: 302px; }

  .headline { position: absolute; left: 56px; font-family: "Bitter", serif; font-weight: 800; color: var(--orange); line-height: 1; white-space: nowrap; }
  .headline--jazz { top: 112px; font-size: 114px; letter-spacing: 2px; }
  .headline--brunch { top: 223px; font-size: 67px; }
  .headline--time { top: 290px; font-size: 54px; font-weight: 700; left: 57px; }
  .flyer--b .headline--jazz { top: 131px; }
  .flyer--b .headline--brunch { top: 242px; }
  .flyer--b .headline--time { top: 309px; }

  .tagline { position: absolute; left: 59px; top: 352px; font-family: "Cabin", sans-serif; font-weight: 600; font-size: 17.5px; color: var(--ink); letter-spacing: 0.2px; }
  .flyer--b .tagline { top: 370px; }

  .dates { position: absolute; left: 0; top: 409px; width: 100%; height: 88px; background: var(--brown); display: flex; align-items: center; }
  .flyer--b .dates { top: 425px; }
  .date { flex: 1; text-align: center; font-family: "Cabin", sans-serif; font-weight: 500; line-height: 1.12; }
  .date + .date { border-left: 1.5px solid var(--light); }
  .date__day { color: var(--orange); font-size: 17px; }
  .date__band { color: var(--light); font-size: 18px; }
  .date { padding: 6px 0; }

  .brand { font-family: "Bitter", serif; font-weight: 700; color: var(--ink); white-space: nowrap; display: flex; align-items: center; gap: 5px; }
  .brand__dot { width: 8px; height: 8px; border-radius: 50%; background: var(--ink); }
  .footer { position: absolute; left: 0; width: 100%; font-family: "Cabin", sans-serif; font-weight: 500; color: var(--ink); }
  .footer--a { top: 518px; display: flex; align-items: center; justify-content: center; gap: 12px; }
  .footer--a .brand { font-size: 11px; }
  .social { font-size: 8.4px; line-height: 1.35; letter-spacing: 0.2px; }
  .footer--b { top: 536px; text-align: center; }
  .brand--top { position: absolute; left: 0; width: 100%; top: 52px; justify-content: center; font-size: 17px; }
</style>
</head>
<body>
<main class="canvas">

  <article class="flyer flyer--a">
    <div class="art art--sax" role="img" aria-label="Skizze eines Saxophons"></div>
    <div class="art art--reed" role="img" aria-label="Skizze eines Mundstücks"></div>
    <div class="art art--tuba" role="img" aria-label="Skizze einer Tuba"></div>
    <h1 class="headline headline--jazz">JAZZ</h1>
    <p class="headline headline--brunch">BRUNCH</p>
    <p class="headline headline--time">10 – 13 Uhr</p>
    <div class="art art--cup" role="img" aria-label="Skizze einer Kaffeetasse"></div>
    <p class="tagline">LIVE JAZZ MUSIK MIT FRÜHSTÜCK</p>
    <section class="dates">
      <div class="date"><div class="date__day">27.06.20</div><div class="date__band">NAME BAND</div></div>
      <div class="date"><div class="date__day">28.06.20</div><div class="date__band">NAME BAND</div></div>
      <div class="date"><div class="date__day">29.06.20</div><div class="date__band">NAME BAND</div></div>
    </section>
    <footer class="footer footer--a">
      <div class="brand"><span class="brand__dot"></span>Café Seeblick Moor</div>
      <div class="social">INSTAGRAM: CAFESEEBLICKMOOR<br>FACEBOOK: CAFÉ SEEBLICK MOOR</div>
    </footer>
  </article>

  <article class="flyer flyer--b">
    <div class="art art--sax" role="img" aria-label="Skizze eines Saxophons"></div>
    <div class="art art--reed" role="img" aria-label="Skizze eines Mundstücks"></div>
    <div class="brand brand--top"><span class="brand__dot"></span>Café Seeblick Moor</div>
    <div class="art art--tuba" role="img" aria-label="Skizze einer Tuba"></div>
    <h1 class="headline headline--jazz">JAZZ</h1>
    <p class="headline headline--brunch">BRUNCH</p>
    <p class="headline headline--time">10 – 13 Uhr</p>
    <div class="art art--cup" role="img" aria-label="Skizze einer Kaffeetasse"></div>
    <p class="tagline">LIVE JAZZ MUSIK MIT FRÜHSTÜCK</p>
    <section class="dates">
      <div class="date"><div class="date__day">27.06.20</div><div class="date__band">NAME BAND</div></div>
      <div class="date"><div class="date__day">28.06.20</div><div class="date__band">NAME BAND</div></div>
      <div class="date"><div class="date__day">29.06.20</div><div class="date__band">NAME BAND</div></div>
    </section>
    <footer class="footer footer--b">
      <p class="social">INSTAGRAM: CAFESEEBLICKMOOR · FACEBOOK: CAFÉ SEEBLICK MOOR</p>
    </footer>
  </article>

</main>
</body>
</html>
```